Letterhead Design Project

I need a simple, clean and corporate letterhead & follow-on letterhead.
The follow-on letterhead should just have the logo only.
Final File Specs:
Full Bleed Size (starting document size)
213 x 300 mm
2517 x 3544 pixels
* Finished artwork should use the full bleed dimensions for best results.
Document Trim Size (final size after being cut)
210 x 297 mm
2480 x 3508 pixels
* Please be sure to keep all text within the safe margin.
Resolution 300 DPI
Accepted file types:-
Adobe Acrobat 9 Document (*.pdf) (recommended)
Adobe Illustrator CS3 Artwork (*.ai) (recommended)
Adobe Photoshop CS3 Image (*.psd) (recommended)
Bitmap Image (*.bmp)
GIF Image (*.gif)
JPEG Image (*.jpg,*.jpeg)
Microsoft PowerPoint 2010 Document (*.ppt)
Microsoft Publisher 2010 Document (*.pub)
Microsoft Word 2010 Document (*.doc)
PCX Image (*.pcx)
PICT Image (*.pic,*.pict,*.pct)
PNG Image (*.png)
PostScript Document (*.ps)
TIF Image (*.tif,*.tiff)
Windows Enhanced Metafile (*.emf)
Windows Metafile (*.wmf)
Requirements
Must have
- My letterhead must have:-
- Logo
- ACN - 482 617 309
- address - Suite 8, 51 Hartwell Ave, Coogee, NSW 2034
- phone - (02) 8371 5926
- fax - (02) 8352 6149
- email - info@brantorguard.com.au
- web - www.brantorguard.com.au
Follow-on letterhead should have the logo only

```html
<!DOCTYPE html>
<html lang="en">
<head>
<meta charset="utf-8">
<title>Brantor Guard Letterhead</title>
<link rel="stylesheet" href="https://fonts.googleapis.com/css2?family=Questrial&display=swap">
<style>
  :root {
    --brand-green: #8dc63f;
    --brand-navy: #312a4f;
    --paper: #ffffff;
    --footer-text: #ffffff;
  }
  html, body {
    margin: 0;
    padding: 0;
    overflow: hidden;
    background: var(--paper);
  }
  .letterhead {
    position: relative;
    width: 884px;
    height: 1200px;
    background: var(--paper);
    overflow: hidden;
    font-family: "Questrial", "Century Gothic", sans-serif;
  }
  .brand {
    position: absolute;
    left: 14px;
    top: 40px;
    display: flex;
    align-items: center;
    gap: 12px;
  }
  .brand-mark {
    width: 40px;
    height: 40px;
    background: var(--brand-navy);
  }
  .brand-name {
    margin: 0;
    font-size: 44px;
    font-weight: 400;
    line-height: 1;
    color: var(--brand-green);
    letter-spacing: -0.5px;
  }
  .footer-rule {
    position: absolute;
    left: 0;
    top: 1094px;
    width: 100%;
    height: 13px;
    background: var(--brand-navy);
  }
  .footer {
    position: absolute;
    left: 0;
    top: 1107px;
    width: 100%;
    height: 93px;
    background: var(--brand-green);
    color: var(--footer-text);
    text-align: center;
    font-size: 14.5px;
    line-height: 17.4px;
    padding-top: 2px;
    box-sizing: border-box;
  }
  .footer p { margin: 0; }
  .footer .gap { display: inline-block; width: 50px; }
</style>
</head>
<body>
  <main class="letterhead">
    <header class="brand">
      <span class="brand-mark" aria-hidden="true"></span>
      <h1 class="brand-name">Brantor Guard</h1>
    </header>

    <div class="footer-rule" aria-hidden="true"></div>
    <footer class="footer">
      <p>ACN : 482 617 309</p>
      <p>address: Suite 8, 51 Hartwell Ave, Coogee, NSW 2034</p>
      <p>phone: (02) 8371 5926<span class="gap"></span>Fax: (02) 8352 6149</p>
      <p>Email: info@brantorguard.com.au</p>
      <p>www.brantorguard.com.au</p>
    </footer>
  </main>
</body>
</html>
```